Brightmoor Senior Living Marketing Brochure, Covid-19 Brochure, Introduction to our manager

We are a Senior Living Community that services Assisted living and memory care. We have a lot of New programs for Activities, Food recipes, therapy, family and resident interaction , covid free, and want to introduce this to the community and existing family members.

Target Market(s)

La Jolla and San Diego for Brightmoor Senior Living and Memory Care of La Jolla and For Brightmoor Senior Living and Memory Care of Tarzana , San Fernando valley, tarzana, Encino , Woodland Hills Sherman oaks

Industry/Entity Type

Assisted Living

Font styles to use

Colors
a54499
f7f3f9
ffffff
fece3e
ffc214

Requirements
Must have
• Product names for our marketing brochure , facility images per location

```html
<!DOCTYPE html>
<html lang="en">
<head>
<meta charset="utf-8">
<title>Brightmoor Senior Living Brochure</title>
<link href="https://fonts.googleapis.com/css2?family=Cinzel:wght@400;600&family=Source+Sans+3:wght@400;600;700&display=swap" rel="stylesheet">
<style>
:root{
  --magenta:#9b1c6e;
  --magenta-dark:#7e1559;
  --gold:#cfb252;
  --gold-light:#dcc574;
  --cream:#f4ead0;
  --paper:#fbf9f6;
  --white:#ffffff;
  --ink:#4a4a4a;
  --stage:#e9e9ea;
  --serif:'Cinzel',serif;
  --sans:'Source Sans 3',sans-serif;
}
*{box-sizing:border-box;margin:0;padding:0}
html,body{width:761px;height:1200px;overflow:hidden}
body{background:var(--stage);font-family:var(--sans);color:var(--ink);position:relative}
.sheet{position:absolute;left:53px;width:654px;height:508px;display:flex;box-shadow:0 10px 14px -6px rgba(0,0,0,.35)}
.sheet.outside{top:60px}
.sheet.inside{top:606px}
.panel{position:relative;width:218px;height:100%;overflow:hidden}
.photo{position:absolute;background:linear-gradient(135deg,#b59a82,#d9c4a8 55%,#8f7a64)}
.fill{position:absolute;inset:0;width:100%;height:100%}
.wordmark{font-family:var(--serif);color:var(--gold);text-align:center;letter-spacing:1px}
.wordmark .dot{display:inline-block;width:7px;height:7px;border-radius:50%;background:var(--magenta);margin-right:4px;vertical-align:middle}
.wordmark small{display:block;font-size:5.5px;letter-spacing:1.2px;margin-top:1px}
.band{position:absolute;left:0;right:0;bottom:6px;height:20px;background:var(--magenta);color:var(--white);font-size:9px;display:flex;align-items:center;justify-content:center}

/* outside, left */
.amenities{background:linear-gradient(90deg,#f6f2ee,var(--white))}
.amenities .wordmark{position:absolute;top:40px;left:18px;font-size:15px;text-align:left}
.amenities .lead{position:absolute;top:86px;left:18px;right:10px;font-size:8.6px;line-height:13.6px;color:var(--magenta)}
.amenity-list{position:absolute;top:150px;left:18px;right:4px;list-style:none;font-size:7.6px;line-height:13.8px}
.amenity-list li{position:relative;padding-left:15px}
.amenity-list li::before{content:"";position:absolute;left:1px;top:3.5px;width:5px;height:5px;border:1px solid var(--magenta);border-radius:50%}

/* outside, middle */
.contact{background:linear-gradient(170deg,#a42579,var(--magenta) 60%,var(--magenta-dark))}
.contact .gold-base{position:absolute;left:0;top:0;width:218px;height:508px}
.contact .mark-dot{position:absolute;top:20px;left:102px;width:14px;height:14px;border-radius:50%;background:var(--gold)}
.contact h1{position:absolute;top:60px;left:0;right:0;font-family:var(--serif);font-weight:400;font-size:11.4px;line-height:16px;color:var(--cream);text-align:center;letter-spacing:.4px}
.contact .region{position:absolute;top:99px;left:0;right:0;text-align:center;color:var(--white);font-size:10px}
.location{position:absolute;top:122px;width:80px;text-align:center;color:var(--white);font-size:5.3px;line-height:7.4px}
.location .photo{position:relative;width:76px;height:59px;margin:0 auto 4px;border:2px solid var(--white);background:linear-gradient(160deg,#9cc0dd,#d9c6a6 55%,#b58c62)}
.location.tarzana{left:20px}
.location.lajolla{left:118px}
.contact .call{position:absolute;top:221px;left:0;right:0;font-family:var(--serif);font-size:15px;color:var(--white);text-align:center;letter-spacing:.6px}
.phone-pill{position:absolute;top:257px;left:40px;width:140px;height:20px;border-radius:10px;background:var(--gold-light);color:var(--white);font-size:11px;font-weight:600;letter-spacing:.6px;display:flex;align-items:center;justify-content:center;gap:6px}
.hands{position:absolute;top:295px;left:53px;width:112px;height:112px;border-radius:50%;border:3px solid var(--white);background:radial-gradient(circle,#e6d3c4,#c9ad98);overflow:hidden}
.contact .lines{position:absolute;top:416px;left:0;right:0;text-align:center;color:var(--magenta);font-size:8.4px;line-height:11.4px}
.social{position:absolute;top:451px;left:0;right:0;display:flex;justify-content:center;gap:13px}
.social span{width:17px;height:17px;border:1px solid var(--white);border-radius:50%}

/* outside, right */
.cover{background:var(--gold)}
.cover .top{position:absolute;left:0;top:0;width:218px;height:100px;background:var(--white)}
.cover .wordmark{position:absolute;top:37px;left:0;right:0;font-size:20px}
.cover .wordmark small{font-size:7.2px;margin-top:2px}
.cover .tagline{position:absolute;top:421px;left:0;right:0;text-align:center;font-family:var(--serif);color:var(--cream);font-size:14px;line-height:27px;letter-spacing:.8px}

/* inside, left */
.care{background:linear-gradient(180deg,var(--gold),#c9ab48)}
.care .intro{position:absolute;top:36px;left:18px;right:11px;font-size:8.2px;line-height:11.5px;color:var(--white);text-align:justify}
.service{position:absolute;left:18px;right:11px;color:var(--white)}
.service h2{font-size:9.2px;font-weight:700;letter-spacing:.2px;display:flex;align-items:center;gap:6px;margin-bottom:6px}
.service h2 i{width:8px;height:8px;border-radius:50%;background:var(--magenta);display:inline-block}
.service p{font-size:7.6px;line-height:10.4px;text-align:justify}
.care .s1{top:112px}.care .s2{top:178px}.care .s3{top:240px}

/* inside, middle */
.features{background:linear-gradient(90deg,#fdfcf9,#f1ece4)}
.features .wordmark{position:absolute;top:30px;left:0;right:0;font-size:18px}
.thumbs{position:absolute;top:66px;left:17px;display:flex;gap:3px}
.thumbs span{width:61px;height:48px;border:1.5px solid var(--white);background:linear-gradient(140deg,#8e6f63,#c9ae8c 50%,#6c7b55)}
.feature-list{position:absolute;top:124px;left:14px;right:12px;list-style:none;font-size:7.2px;line-height:11.45px}
.feature-list li{padding-left:6px;text-indent:-5px}
.feature-list li::before{content:"• "}
.visit-band{position:absolute;bottom:6px;left:232px;width:422px;height:16px;display:flex;z-index:2}
.visit-band div{flex:1;background:var(--magenta);color:var(--white);font-size:8px;display:flex;align-items:center;justify-content:center;gap:5px}
.visit-band div:first-child{border-radius:8px 0 0 8px}
.visit-band i{width:6px;height:6px;border:1px solid var(--white);border-radius:50%}

/* inside, right */
.programs{background:var(--gold)}
.programs .service{left:16px;right:13px}
.programs .service h2{font-size:8.8px}
.programs .service p{font-size:7.2px;line-height:10.4px}
.programs .p1{top:199px}.programs .p2{top:277px}.programs .p3{top:348px}.programs .p4{top:419px}
</style>
</head>
<body>

<section class="sheet outside">
  <div class="panel amenities">
    <div class="wordmark"><span class="dot"></span>BRIGHTMOOR<small>SENIOR LIVING &amp; MEMORY CARE</small></div>
    <p class="lead">We take great pride in providing top notch services and exceptional amenities for all our residents.</p>
    <ul class="amenity-list">
      <li>Housekeeping And Laundry Services</li>
      <li>Emergency Alert System</li>
      <li>Daily Activity Schedule</li>
      <li>Beauty Salon And Barber Shop</li>
      <li>Luxury Transportation: Marlow Shuttle Vans and Kestrel Minivans And Valet Services</li>
      <li>General Store</li>
      <li>Skyline TV Premium Package – Premium Sports Package, CinemaMax, ReelTime And More!</li>
      <li>Movie Theatre, Shuffle Board, Pool Table And Outdoor BBQ</li>
      <li>Virtual Reality Station.</li>
      <li>Salon for nails hair and massages</li>
    </ul>
    <svg class="fill" viewBox="0 0 218 508" preserveAspectRatio="none" aria-hidden="true">
      <path d="M0 355 Q90 318 218 330 L218 508 L0 508Z" fill="var(--cream)"/>
    </svg>
    <svg class="fill" viewBox="0 0 218 508" preserveAspectRatio="none" role="img" aria-label="Photo of senior women sharing tea at a table with flowers">
      <defs><linearGradient id="teaPhoto" x1="0" y1="0" x2="1" y2="1"><stop offset="0" stop-color="#cdbba3"/><stop offset=".5" stop-color="#a88866"/><stop offset="1" stop-color="#7d5d47"/></linearGradient></defs>
      <path d="M0 368 Q90 330 218 340 L218 508 L0 508Z" fill="url(#teaPhoto)"/>
    </svg>
  </div>

  <div class="panel contact">
    <svg class="gold-base" viewBox="0 0 218 508" preserveAspectRatio="none" aria-hidden="true">
      <path d="M0 330 Q110 300 218 350 L218 508 L0 508Z" fill="var(--gold)"/>
    </svg>
    <span class="mark-dot"></span>
    <h1>BRIGHTMOOR SENIOR<br>LIVING AND MEMORY CARE</h1>
    <p class="region">Southern California Locations</p>
    <div class="location tarzana">
      <div class="photo" role="img" aria-label="Photo of the Tarzana community building"></div>
      Tarzana, California<br>(818) 555-0142<br>4120 Oakcrest Avenue
    </div>
    <div class="location lajolla">
      <div class="photo" role="img" aria-label="Photo of the La Jolla community entrance"></div>
      La Jolla, California<br>(858) 555-0187<br>7350 Seabright Ave
    </div>
    <p class="call">CALL US TODAY:</p>
    <div class="phone-pill">
      <svg width="12" height="12" viewBox="0 0 24 24" aria-hidden="true"><circle cx="12" cy="12" r="11" fill="none" stroke="#fff" stroke-width="2"/><path d="M8 6l2 0 1 3-1.5 1a7 7 0 0 0 3.5 3.5L14 12l3 1v2c0 1-1 2-2 2A9 9 0 0 1 7 8c0-1 .5-2 1-2z" fill="#fff"/></svg>
      (818) 555-0142
    </div>
    <div class="hands" role="img" aria-label="Close-up photo of caring hands holding an elderly hand"></div>
    <p class="lines">+1 818-555-0142<br>jmarsh@brightmoorliving.com<br>www.brightmoorliving.com</p>
    <div class="social" aria-hidden="true"><span></span><span></span><span></span><span></span></div>
    <div class="band">www.brightmoorliving.com</div>
  </div>

  <div class="panel cover">
    <div class="top"></div>
    <div class="wordmark"><span class="dot"></span>BRIGHTMOOR<small>SENIOR LIVING &amp; MEMORY CARE</small></div>
    <svg class="fill" viewBox="0 0 218 508" preserveAspectRatio="none" aria-hidden="true">
      <path d="M0 98 Q110 84 218 92 L218 400 L0 370Z" fill="var(--cream)"/>
    </svg>
    <svg class="fill" viewBox="0 0 218 508" preserveAspectRatio="none" role="img" aria-label="Photo of a smiling senior couple sitting on a garden bench">
      <defs><linearGradient id="coupleBench" x1="0" y1="0" x2="1" y2="1"><stop offset="0" stop-color="#a8523c"/><stop offset=".5" stop-color="#c7b8a8"/><stop offset="1" stop-color="#7b6a54"/></linearGradient></defs>
      <path d="M0 106 Q110 92 218 100 L218 386 Q110 395 0 356Z" fill="url(#coupleBench)"/>
    </svg>
    <p class="tagline">A LUXURIOUS SENIOR<br>LIVING COMMUNITY</p>
    <div class="band">www.brightmoorliving.com</div>
  </div>
</section>

<section class="sheet inside">
  <div class="panel care">
    <p class="intro">At Brightmoor, we know that each senior who comes through our doors has a unique set of interests and needs. We provide living arrangements that suit your lifestyle with various levels of care and personal assistance.</p>
    <div class="service s1"><h2><i></i>INDEPENDENT LIVING</h2><p>Our independent living community provides older adults with everything they need to maintain their independence as they age.</p></div>
    <div class="service s2"><h2><i></i>ASSISTED CARE</h2><p>At Brightmoor Senior Living and Memory Care the outstanding, comprehensive, licensed assisted living program is the hallmark of our service.</p></div>
    <div class="service s3"><h2><i></i>MEMORY CARE</h2><p>At Brightmoor Senior Living and Memory Care, our caregivers give residents and their families the support they need for living with memory loss.</p></div>
    <svg class="fill" viewBox="0 0 218 508" preserveAspectRatio="none" aria-hidden="true">
      <path d="M0 312 Q110 300 218 330 L218 508 L0 508Z" fill="var(--cream)"/>
    </svg>
    <svg class="fill" viewBox="0 0 218 508" preserveAspectRatio="none" role="img" aria-label="Photo of a caregiver with a senior woman in a wheelchair">
      <defs><linearGradient id="caregiver" x1="0" y1="0" x2="1" y2="1"><stop offset="0" stop-color="#5b7aa6"/><stop offset=".5" stop-color="#e0cdb8"/><stop offset="1" stop-color="#8b8c86"/></linearGradient></defs>
      <path d="M0 322 Q110 310 218 340 L218 508 L0 508Z" fill="url(#caregiver)"/>
    </svg>
  </div>

  <div class="panel features">
    <div class="wordmark"><span class="dot"></span>BRIGHTMOOR<small>SENIOR LIVING &amp; MEMORY CARE</small></div>
    <div class="thumbs" role="img" aria-label="Three photos of resident activities: dining, putting green and friends together"><span></span><span></span><span></span></div>
    <ul class="feature-list">
      <li>Multiple Resident Assessments based on Service Types</li>
      <li>Resident Task Scheduling and Service Plans</li>
      <li>End of Shift Reporting</li>
      <li>Resident Care Threads</li>
      <li>Resident Focus Areas and Incident Tracking and Reporting</li>
      <li>Meaningful and Customizable Dashboards</li>
      <li>Availability of standardized Focus Areas and Follow up Protocols</li>
      <li>Cost of Care Variance Reporting</li>
      <li>customized Assessments (based on flexible points, time, or flat rate)</li>
      <li>eMAR</li>
      <li>Acuity Analysis</li>
      <li>State Forms and Reporting</li>
      <li>Scheduled care (includes non-assessment related tasks such as physician visits, TB testing, etc.)</li>
      <li>Acuity levels</li>
      <li>Staffing needs analysis for your Assisted Living, Memory Care or CCRC community is based on up-to-date resident assessments. Document resident risks, past incidents, individual behaviors, preferences, and additional family and caregiver input.</li>
      <li>Family and Resident Portal</li>
      <li>Brightmoor Senior Living is overcoming social isolation through the power of virtual reality and shared experiences.</li>
    </ul>
  </div>

  <div class="panel programs">
    <svg class="fill" viewBox="0 0 218 508" preserveAspectRatio="none" aria-hidden="true">
      <path d="M0 0 L218 0 L218 172 Q100 200 0 172Z" fill="var(--cream)"/>
    </svg>
    <svg class="fill" viewBox="0 0 218 508" preserveAspectRatio="none" role="img" aria-label="Photo of a senior couple embracing outdoors">
      <defs><linearGradient id="embrace" x1="0" y1="0" x2="1" y2="1"><stop offset="0" stop-color="#c9c6a0"/><stop offset=".5" stop-color="#d4b69a"/><stop offset="1" stop-color="#6f8aa8"/></linearGradient></defs>
      <path d="M0 0 L218 0 L218 164 Q100 190 0 162Z" fill="url(#embrace)"/>
    </svg>
    <div class="service p1"><h2><i></i>LIVING - RELIVE</h2><p>Customized reminiscence therapy tools allow your residents to take a stroll down memory lane by revisiting their childhood home, wedding location or anywhere else from their past.</p></div>
    <div class="service p2"><h2><i></i>CONNECT - RECONNECT</h2><p>Provide opportunities for your loved ones to virtually leave the four walls of our community to check off bucket list items and engage with the world in ways they never thought possible.</p></div>
    <div class="service p3"><h2><i></i>LIGHTBULB - REINSPIRE</h2><p>Create new friendships through the power of shared experience, all while providing unforgettable moments and stories that residents and their families will remember forever.</p></div>
    <div class="service p4"><h2><i></i>FAMILY MEMBERS</h2><p>Normally, you can't control how much stimulation your loved one experiences everyday. You can trust that a our community thinks of resident happiness first.</p></div>
  </div>

  <div class="visit-band">
    <div>Visit our website for more information</div>
    <div><i></i>www.brightmoorliving.com</div>
  </div>
</section>

</body>
</html>
```